For Creative Minds: A Simple Clean Book Cover that Stands Out

This will be a christian book teaching christians about divine healing. It is part of a series called "Forty Morning Set". I want the book cover to communicate the idea of healing, and specifically heavenly healing from God. These are some of the specifications below

1. General
Book to be published on print lantern platform
Dimensions: 6 x 9 inches, Paperback
Number of words: Estimated to be about 60,000 words.
Please use Indesign for design and submit the final Indesign source files along with the final design.

2. Cover image.
Image can be either human or any object that can communicate the idea above. No human faces to show up prominently.
High quality image is highly solicited.

3. Title:
" Forty Mornings to Claim and Hold Your Heavenly Restoration"

3. Author name
Preferably should appear below. Open to creative ideas with titles that are better placed above.

Author's Name: Daniel Fesch

3. Layout
Should not be too busy.
Simple and clean layout appeals more to me.

4. Series name
AS noted above, this book will be part of a series called " Forty Morning Set". I want this series name to appear somewhere in the cover and to have a simple but unique design that will be used for all subsequent titles. The Title of the book should have the emphasis.

I have attached a sample cover for one of my monthly devotional books which I choose from a contest.

ABOUT THE AUTHOR
Daniel Fesch represents the blessed combination of Physician and Minister, bringing healing not only to the physical body but to the spiritual heart. He currently works as the Director of the Hospital Medicine Program at the Brellmont County Care Campus in Iowa, USA. He is the Founder of Lantern & Vine Fellowship, a teaching ministry that seeks to bring believers into the fullness of grace — the glory of God — through conferences, seminars and books.

One of his notable quotes is “The Word of God is the most potent and efficient remedy for all the ailments of humanity.” This clearly portrays his experience with the Word as a Physician who is familiar with the powers, both natural and supernatural, to mend broken human beings. 

He currently lives in Iowa, USA with his wife, Tessa Lund, and daughter, Rosalind. You can reach out to Daniel using the contact information listed below.

BLURB
As a Physician and Minister, I have seen the power of modern medicine to bring about healing in the body and mind as well as the operation of the power of God to produce amazing medical results. However, many people are just not aware of the reality of divine healing. To some, it is a myth, belief or some "faith talk" in the heart. Medical miracles are real and we should take full advantage of it. As much as a love being a physician and treat patients in the hospital, I have come to see both its amazing successes and many limitations.

Industry/Entity Type

Christian

Font styles to use
Serif

Colors

Designer to choose colors to be used in the design.

Requirements
Should not have
• Too stylistic fonts

```html
<!DOCTYPE html>
<html lang="en">
<head>
<meta charset="utf-8">
<title>Forty Mornings to Claim and Hold Your Heavenly Restoration — Cover Wrap</title>
<link rel="stylesheet" href="https://fonts.googleapis.com/css2?family=Playfair+Display:wght@700&family=Libre+Baskerville:wght@700&display=swap">
<style>
  :root {
    --wood-deep: #6a3026;
    --wood-mid: #8a4837;
    --wood-light: #b0705a;
    --mist: #f6ecf4;
    --lavender: #c8a6c6;
    --dusk: #9a6a86;
    --gold: #d9a56c;
    --bark: #5a2f2a;
    --cream: #fdf6ee;
    --ink: #3a1c16;
    --shadow: rgba(55, 18, 10, 0.55);
    --spine-line: rgba(40, 14, 8, 0.45);
  }
  * { margin: 0; padding: 0; box-sizing: border-box; }
  html, body { width: 1200px; height: 900px; overflow: hidden; background: var(--wood-deep); }

  .cover-wrap { position: relative; width: 1200px; height: 900px; }

  .back-cover {
    position: absolute; left: 0; top: 0; width: 600px; height: 900px;
    background:
      linear-gradient(120deg, rgba(0,0,0,0) 55%, rgba(200,135,100,0.35) 75%, rgba(0,0,0,0) 90%),
      linear-gradient(125deg, rgba(190,120,95,0.35) 0%, rgba(0,0,0,0) 45%),
      linear-gradient(180deg, var(--wood-light) 0%, var(--wood-mid) 35%, var(--wood-deep) 100%);
  }
  .front-cover { position: absolute; left: 600px; top: 0; width: 600px; height: 900px; }
  .front-photo {
    position: absolute; inset: 0;
    background:
      radial-gradient(ellipse 170px 150px at 300px 150px, var(--mist) 0%, rgba(246,236,244,0.75) 45%, rgba(0,0,0,0) 100%),
      linear-gradient(100deg, rgba(0,0,0,0) 70%, rgba(217,165,108,0.55) 86%, rgba(90,47,42,0.5) 100%),
      linear-gradient(90deg, rgba(90,47,42,0.25) 0%, rgba(0,0,0,0) 12%),
      linear-gradient(180deg, var(--lavender) 0%, #b88ca8 30%, var(--dusk) 48%, var(--wood-mid) 72%, var(--wood-deep) 100%);
  }
  .spine-line { position: absolute; left: 599px; top: 0; width: 1px; height: 900px; background: var(--spine-line); }

  .title-block { position: absolute; color: var(--cream); text-shadow: 1px 2px 3px var(--shadow); }
  .title-lead, .title-big, .title-last {
    display: block; font-family: "Playfair Display", Georgia, serif; font-weight: 700; white-space: nowrap;
  }
  .title-lead { font-size: 2.75em; line-height: 1.05; }
  .title-big { font-size: 5em; line-height: 1; margin-top: 0.02em; }
  .title-last { font-size: 3.9em; line-height: 1; }
  .title-sub {
    display: block; font-family: "Libre Baskerville", Georgia, serif; font-weight: 700;
    font-size: 0.95em; letter-spacing: 0.02em; line-height: 1.1; margin-top: 0.35em; white-space: nowrap;
  }
  .title-sub.align-right { text-align: right; font-size: 1.2em; margin-top: 0.05em; }

  .series-band {
    display: block; margin-top: 0.5em; width: 80%;
    background: linear-gradient(90deg, rgba(253,246,238,0.2) 0%, rgba(253,246,238,0.95) 22%, rgba(253,246,238,0.95) 78%, rgba(253,246,238,0.2) 100%);
    color: var(--ink); text-shadow: none; text-align: center;
    font-family: "Libre Baskerville", Georgia, serif; font-weight: 700; font-size: 0.85em;
    letter-spacing: 0.04em; padding: 0.2em 0;
  }

  .front-title { left: 221px; top: 505px; width: 336px; font-size: 16px; }
  .front-author {
    position: absolute; right: 45px; top: 50px; color: var(--cream);
    font-family: "Libre Baskerville", Georgia, serif; font-weight: 700; font-size: 19px;
    text-shadow: 1px 2px 3px var(--shadow);
  }

  .back-panel {
    position: absolute; left: 157px; top: 310px; width: 288px; height: 279px;
    border-radius: 14px; background: rgba(255, 245, 240, 0.32);
  }
  .back-title { left: 18px; top: 14px; width: 253px; font-size: 12px; }
  .back-author {
    position: absolute; right: 14px; bottom: 16px; color: var(--cream);
    font-family: "Libre Baskerville", Georgia, serif; font-weight: 700; font-size: 15px;
    text-shadow: 1px 1px 2px var(--shadow);
  }
</style>
</head>
<body>
<div class="cover-wrap">

  <section class="back-cover" role="img" aria-label="Photo of a wooden boardwalk bridge in warm reddish-brown light">
    <div class="back-panel">
      <div class="title-block back-title">
        <span class="title-lead">Forty Mornings</span>
        <span class="title-sub">TO CLAIM AND HOLD</span>
        <span class="title-sub align-right">YOUR</span>
        <span class="title-big">Heavenly</span>
        <span class="title-last">Restoration</span>
        <span class="series-band">FORTY MORNING SET</span>
      </div>
      <p class="back-author">—Daniel Fesch</p>
    </div>
  </section>

  <section class="front-cover">
    <div class="front-photo" role="img" aria-label="Photo of a woman in silhouette with arms outstretched on a misty wooden bridge, glowing light ahead through the trees"></div>
    <p class="front-author">—Daniel Fesch</p>
    <h1 class="title-block front-title">
      <span class="title-lead">Forty Mornings</span>
      <span class="title-sub">TO CLAIM AND HOLD</span>
      <span class="title-sub align-right">YOUR</span>
      <span class="title-big">Heavenly</span>
      <span class="title-last">Restoration</span>
      <span class="series-band">FORTY MORNING SET</span>
    </h1>
  </section>

  <div class="spine-line"></div>
</div>
</body>
</html>
```